Business Card Project

We are a small consulting firm. You can experiment with any design.
Must have:
1) Company name - TOLVIN International
2) Company slogan - simple solutions for complex problems
3) Name/Title/Phone/Email/WWW/ - use anything you like as an example.

Industry/Entity Type

Business

```html
<!DOCTYPE html>
<html lang="en">
<head>
<meta charset="utf-8">
<title>TOLVIN International – Business Card</title>
<link rel="stylesheet" href="https://fonts.googleapis.com/css2?family=Open+Sans:wght@400;600;700&display=swap">
<style>
  :root {
    --page: #2b2b2c;
    --card: #5c5d5f;
    --card-map: #66676a;
    --lime: #a8c83a;
    --white: #ffffff;
    --text-light: #f2f2f2;
  }
  * { box-sizing: border-box; margin: 0; padding: 0; }
  html, body {
    width: 1200px; height: 900px; overflow: hidden;
    background: var(--page);
    font-family: "Open Sans", sans-serif;
  }
  .stage { position: relative; width: 1200px; height: 900px; }
  .card {
    position: absolute; top: 304px;
    width: 530px; height: 292px;
    background: var(--card);
    border-radius: 18px;
    overflow: hidden;
    box-shadow: 0 6px 14px rgba(0,0,0,.45);
  }
  .card--front { left: 55px; }
  .card--back { left: 615px; }

  .wordmark { position: absolute; left: 0; right: 0; text-align: center; color: var(--lime); font-weight: 400; line-height: 1; }
  .wordmark__name { display: block; letter-spacing: 6px; }
  .wordmark__sub { display: block; letter-spacing: 12px; margin-top: 18px; font-size: 11px; padding-left: 12px; }
  .card--front .wordmark { top: 88px; }
  .card--front .wordmark__name { font-size: 74px; }
  .card--back .wordmark { top: 34px; }
  .card--back .wordmark__name { font-size: 72px; }

  .slogan-band {
    position: absolute; left: 0; right: 0; top: 235px; height: 28px;
    background: var(--lime);
    color: var(--white);
    font-size: 14px; letter-spacing: 2.2px;
    display: flex; align-items: center; justify-content: center;
    text-transform: uppercase;
  }

  .map-area {
    position: absolute; left: 18px; top: 22px; width: 495px; height: 258px;
    background: radial-gradient(ellipse at 50% 50%, var(--card-map) 0%, var(--card) 75%);
    border-radius: 12px;
  }

  .contact-person { position: absolute; left: 44px; top: 175px; color: var(--text-light); }
  .contact-person__name { color: var(--lime); font-size: 19px; font-weight: 600; line-height: 1.2; }
  .contact-person__title { font-size: 14px; font-weight: 700; margin-top: 2px; }
  .contact-list { list-style: none; font-size: 12.5px; line-height: 18px; color: var(--text-light); }
  .contact-person .contact-list { margin-top: 16px; }
  .contact-list li { display: flex; align-items: flex-start; gap: 6px; }
  .contact-list svg { flex: none; width: 10px; height: 10px; margin-top: 4px; fill: var(--lime); }
  .contact-address { position: absolute; left: 313px; top: 180px; }
</style>
</head>
<body>
<main class="stage">

  <section class="card card--front" aria-label="Business card front">
    <div class="wordmark">
      <span class="wordmark__name">TOLVIN</span>
      <span class="wordmark__sub">INTERNATIONAL</span>
    </div>
    <div class="slogan-band">Simple solutions for complex problems</div>
  </section>

  <section class="card card--back" aria-label="Business card back">
    <div class="map-area" role="img" aria-label="Faint world map in the background"></div>
    <div class="wordmark">
      <span class="wordmark__name">TOLVIN</span>
      <span class="wordmark__sub">INTERNATIONAL</span>
    </div>

    <div class="contact-person">
      <p class="contact-person__name">Daniel Marsh</p>
      <p class="contact-person__title">managing director</p>
      <ul class="contact-list">
        <li><svg viewBox="0 0 10 10" aria-hidden="true"><path d="M2 0.5 L3.6 2.6 L2.7 3.6 Q4 6 6.4 7.3 L7.4 6.4 L9.5 8 L8.2 9.5 Q4.5 9.3 1.5 5.5 Q0.2 3.3 0.5 1.8 Z"/></svg>777 240 18 36</li>
        <li><svg viewBox="0 0 10 10" aria-hidden="true"><path d="M2.5 0 H7.5 V10 H2.5 Z M3.3 1 V8 H6.7 V1 Z"/></svg>777 240 18 37</li>
      </ul>
    </div>

    <ul class="contact-list contact-address">
      <li><svg viewBox="0 0 10 10" aria-hidden="true"><path d="M5 0 A3.6 3.6 0 0 1 8.6 3.6 C8.6 6 5 10 5 10 C5 10 1.4 6 1.4 3.6 A3.6 3.6 0 0 1 5 0 Z M5 2.2 A1.4 1.4 0 1 0 5 5 A1.4 1.4 0 1 0 5 2.2 Z"/></svg>48 Harbor Lane<br>Millbrook, New York 12545<br>Suite 12</li>
      <li><svg viewBox="0 0 10 10" aria-hidden="true"><path d="M0 2 H10 V8.5 H0 Z M0.8 2.6 L5 5.6 L9.2 2.6 V2.4 H0.8 Z" fill-rule="evenodd"/></svg>info@tolvinint.com</li>
      <li><svg viewBox="0 0 10 10" aria-hidden="true"><path d="M5 0.5 A4.5 4.5 0 1 0 5 9.5 A4.5 4.5 0 1 0 5 0.5 Z M5 1.4 A3.6 3.6 0 1 1 5 8.6 A3.6 3.6 0 1 1 5 1.4 Z M1 4.6 H9 V5.4 H1 Z M4.6 1 H5.4 V9 H4.6 Z"/></svg>www.tolvinint.com</li>
    </ul>
  </section>

</main>
</body>
</html>
```